photowall advertisement

We require a wall featuring our company logo. We would like to avoid the color green, and gold is highly preferred. The design should be similar to the one in the attached photo. The wall will be used for photos and promotional purposes during congresses. Files must be prepared for printing.
dimension of wall: 470x223 cm

Industry/Entity Type

lifestyle

Colors
0054AA
0677BA
7BADD7
CADEEF
E8F1F8
6B429C
8869AF
B7A5CE
E3DAEB
F3F0F8

Requirements
Must have
• gold color, white, and other compare with gold color
Nice to have
• some pictograms, maps of Europe

```html
<!DOCTYPE html>
<html lang="en">
<head>
<meta charset="utf-8">
<title>Quorvane Technology – Photo Wall</title>
<link rel="stylesheet" href="https://fonts.googleapis.com/css2?family=Michroma&display=swap">
<style>
  :root {
    --stage: #dcdddf;
    --wall: #ffffff;
    --ink: #111111;
    --gold-light: #e6c21a;
    --gold: #c39a1f;
    --gold-deep: #8a4a12;
    --map-tone: #eeeeee;
  }
  html, body {
    margin: 0;
    padding: 0;
    width: 1200px;
    height: 653px;
    overflow: hidden;
    background: var(--stage);
  }
  .photo-wall {
    position: absolute;
    left: 0;
    top: 41px;
    width: 1200px;
    height: 570px;
    display: block;
    background: var(--wall);
  }
  .brand-name {
    font-family: "Michroma", sans-serif;
    fill: var(--ink);
  }
  .divider {
    stroke: var(--gold);
    stroke-width: 3;
  }
</style>
</head>
<body>
<svg class="photo-wall" viewBox="0 0 1772 841" xmlns="http://www.w3.org/2000/svg" aria-label="Quorvane Technology photo wall">
  <defs>
    <radialGradient id="map-fade" cx="50%" cy="50%" r="50%">
      <stop offset="0%" stop-color="var(--map-tone)"/>
      <stop offset="70%" stop-color="var(--map-tone)" stop-opacity="0.7"/>
      <stop offset="100%" stop-color="var(--map-tone)" stop-opacity="0"/>
    </radialGradient>
    <linearGradient id="gold-frame" x1="0" y1="0" x2="1" y2="0">
      <stop offset="0%" stop-color="var(--gold-deep)"/>
      <stop offset="50%" stop-color="var(--gold-light)"/>
      <stop offset="100%" stop-color="var(--gold-deep)"/>
    </linearGradient>
    <g id="brand-repeat">
      <text class="brand-name" x="0" y="0" font-size="28" textLength="250" lengthAdjust="spacingAndGlyphs">QUORVANE</text>
      <text class="brand-name" x="0" y="22" font-size="12" textLength="250" lengthAdjust="spacing">TECHNOLOGY</text>
    </g>
  </defs>

  <rect width="1772" height="841" fill="var(--wall)"/>

  <rect class="map-area" x="370" y="10" width="1050" height="820" fill="url(#map-fade)" role="img" aria-label="Faint map of Europe in light grey"/>

  <g class="logo-row">
    <use href="#brand-repeat" x="120" y="80"/>
    <use href="#brand-repeat" x="467" y="80"/>
    <use href="#brand-repeat" x="814" y="80"/>
    <use href="#brand-repeat" x="1161" y="80"/>
    <use href="#brand-repeat" x="1508" y="80"/>
    <line class="divider" x1="419" y1="46" x2="419" y2="110"/>
    <line class="divider" x1="765" y1="46" x2="765" y2="110"/>
    <line class="divider" x1="1111" y1="46" x2="1111" y2="110"/>
    <line class="divider" x1="1457" y1="46" x2="1457" y2="110"/>
  </g>

  <g class="logo-row">
    <use href="#brand-repeat" x="14" y="213"/>
    <use href="#brand-repeat" x="361" y="213"/>
    <use href="#brand-repeat" x="708" y="213"/>
    <use href="#brand-repeat" x="1056" y="213"/>
    <use href="#brand-repeat" x="1403" y="213"/>
    <line class="divider" x1="313" y1="178" x2="313" y2="244"/>
    <line class="divider" x1="659" y1="178" x2="659" y2="244"/>
    <line class="divider" x1="1005" y1="178" x2="1005" y2="244"/>
    <line class="divider" x1="1350" y1="178" x2="1350" y2="244"/>
  </g>

  <g class="logo-side">
    <use href="#brand-repeat" x="120" y="357"/>
    <use href="#brand-repeat" x="1508" y="357"/>
    <use href="#brand-repeat" x="14" y="490"/>
    <use href="#brand-repeat" x="1403" y="490"/>
  </g>

  <g class="main-logo">
    <rect x="431" y="340" width="910" height="161" fill="none" stroke="url(#gold-frame)" stroke-width="3"/>
    <text class="brand-name" x="886" y="430" font-size="64" text-anchor="middle" textLength="800" lengthAdjust="spacingAndGlyphs">QUORVANE</text>
    <text class="brand-name" x="886" y="475" font-size="24" text-anchor="middle" letter-spacing="14">TECHNOLOGY</text>
  </g>

  <g class="logo-row">
    <use href="#brand-repeat" x="120" y="632"/>
    <use href="#brand-repeat" x="467" y="632"/>
    <use href="#brand-repeat" x="814" y="632"/>
    <use href="#brand-repeat" x="1161" y="632"/>
    <use href="#brand-repeat" x="1508" y="632"/>
    <line class="divider" x1="419" y1="598" x2="419" y2="664"/>
    <line class="divider" x1="765" y1="598" x2="765" y2="664"/>
    <line class="divider" x1="1111" y1="598" x2="1111" y2="664"/>
    <line class="divider" x1="1457" y1="598" x2="1457" y2="664"/>
  </g>

  <g class="logo-row">
    <use href="#brand-repeat" x="14" y="765"/>
    <use href="#brand-repeat" x="361" y="765"/>
    <use href="#brand-repeat" x="708" y="765"/>
    <use href="#brand-repeat" x="1056" y="765"/>
    <use href="#brand-repeat" x="1403" y="765"/>
    <line class="divider" x1="313" y1="731" x2="313" y2="797"/>
    <line class="divider" x1="659" y1="731" x2="659" y2="797"/>
    <line class="divider" x1="1005" y1="731" x2="1005" y2="797"/>
    <line class="divider" x1="1350" y1="731" x2="1350" y2="797"/>
  </g>
</svg>
</body>
</html>
```